Business Cards Design for the electrical wholesaler: clean bold dynamic :)

We need a business card design that would follow our latest brand guidelines. As an electrical wholesaler we want to bring a fresh look and feel into the industry. The design should be clean bold and dynamic. It should come alive with the renewed energy of our green colour. Our grey colour should keep things balanced and complement the notion of maturity and responsibility. We employ Lato as a corporate font however are not bound by this font and we’re open to interpretation here.

Target Market(s)

Electrical contractors

Industry/Entity Type

Business

Contact Information for Business Card

Logo
Name & Surname: Olena Dovbush
Job Title: Director of Marketing
Email: helen.dovbush@mailvane.example
Cell phone: XXX.XXX.XXXX
Address: 20917 - 87 Ave. Edmonton, AB, Canada. T6K 2R8
Business Phone: 780.555.0187
Website: www.qorvil.example

Font styles to use
Other font styles liked:
• Lato

Requirements
Must have
• Logo & website
Nice to have
• Brand elements - some of them you may find in the attached Brand Guidelines (e.g. three lines on the background signifying "W")

```html
<!DOCTYPE html>
<html lang="en">
<head>
<meta charset="utf-8">
<title>Qorvil Business Card</title>
<link href="https://fonts.googleapis.com/css2?family=Lato:wght@400;700;900&display=swap" rel="stylesheet">
<style>
  :root {
    --green: #6cc02a;
    --green-deep: #5aa81f;
    --grey-dark: #3a3a3c;
    --grey-mid: #6d6e70;
    --grey-line: #cfcfcf;
    --paper: #ffffff;
    --backdrop: #ececec;
  }
  * { box-sizing: border-box; margin: 0; padding: 0; }
  html, body {
    width: 1200px; height: 1135px; overflow: hidden;
    background: var(--backdrop);
    font-family: "Lato", sans-serif;
  }
  .canvas {
    position: relative; width: 1200px; height: 1135px;
    display: flex; flex-direction: column; align-items: center; justify-content: center; gap: 60px;
  }
  .card {
    position: relative; width: 800px; height: 457px;
    box-shadow: 0 6px 22px rgba(0,0,0,0.12);
    overflow: hidden;
  }

  /* Front */
  .card--front { background: var(--paper); }
  .brand {
    position: absolute; left: 90px; top: 70px;
    display: flex; align-items: center; gap: 16px;
  }
  .brand__mark { width: 46px; height: 46px; background: var(--green); }
  .brand__name {
    font-weight: 900; font-size: 62px; line-height: 1; color: var(--grey-dark);
    letter-spacing: -1px;
  }
  .brand__tagline {
    position: absolute; left: 152px; top: 140px;
    font-size: 11px; letter-spacing: 3.4px; color: var(--grey-mid); text-transform: uppercase;
  }
  .person { position: absolute; left: 90px; top: 190px; }
  .person__name {
    font-weight: 700; font-size: 24px; letter-spacing: 1.5px; color: var(--grey-dark); text-transform: uppercase;
  }
  .person__title {
    margin-top: 6px; font-size: 12px; letter-spacing: 2.4px; color: var(--grey-mid); text-transform: uppercase;
  }
  .rule-left {
    position: absolute; left: 0; top: 300px; width: 410px; height: 5px; background: var(--green);
  }
  .divider {
    position: absolute; left: 410px; top: 270px; width: 1px; height: 120px; background: var(--grey-line);
  }
  .contacts {
    position: absolute; left: 436px; top: 274px; list-style: none;
    display: flex; flex-direction: column; gap: 9px;
  }
  .contacts li {
    display: flex; align-items: center; gap: 12px;
    font-size: 14px; color: var(--grey-dark); letter-spacing: 0.3px;
  }
  .contacts svg { width: 18px; height: 18px; flex: none; }
  .base-bar { position: absolute; bottom: 0; height: 12px; }
  .base-bar--green { left: 410px; width: 260px; background: var(--green); }
  .base-bar--grey { left: 670px; width: 130px; background: var(--grey-dark); }

  /* Back */
  .card--back { background: var(--green); }
  .back-texture {
    position: absolute; inset: 0;
    background: linear-gradient(135deg, var(--green) 0%, var(--green-deep) 100%);
  }
  .back-brand {
    position: absolute; inset: 0;
    display: flex; flex-direction: column; align-items: center; justify-content: center; gap: 10px;
  }
  .back-brand__row { display: flex; align-items: center; gap: 16px; }
  .back-brand__mark { width: 50px; height: 50px; background: var(--grey-dark); }
  .back-brand__name {
    font-weight: 900; font-size: 72px; line-height: 1; color: var(--grey-dark); letter-spacing: -1px;
  }
  .back-brand__tagline {
    font-size: 12px; letter-spacing: 4px; color: var(--grey-dark); text-transform: uppercase;
  }
</style>
</head>
<body>
<main class="canvas">

  <section class="card card--front" aria-label="Business card front">
    <div class="brand">
      <span class="brand__mark"></span>
      <span class="brand__name">qorvil</span>
    </div>
    <div class="brand__tagline">Electrical Wholesalers</div>

    <div class="person">
      <div class="person__name">Olena Dovbush</div>
      <div class="person__title">Director of Marketing</div>
    </div>

    <div class="rule-left"></div>
    <div class="divider"></div>

    <ul class="contacts">
      <li>
        <svg viewBox="0 0 18 18"><rect width="18" height="18" rx="3" fill="#6cc02a"/><path d="M5 4.5h2.2l1 2.6-1.3.9a6 6 0 0 0 3.1 3.1l.9-1.3 2.6 1V13c0 .6-.5 1-1 1A9 9 0 0 1 4 5.5c0-.5.4-1 1-1z" fill="#fff"/></svg>
        780.555.0187
      </li>
      <li>
        <svg viewBox="0 0 18 18"><rect width="18" height="18" rx="3" fill="#6cc02a"/><rect x="6" y="3.5" width="6" height="11" rx="1" fill="#fff"/><rect x="7" y="5" width="4" height="7" fill="#6cc02a"/></svg>
        780.555.0142
      </li>
      <li>
        <svg viewBox="0 0 18 18"><rect width="18" height="18" rx="3" fill="#6cc02a"/><rect x="3.5" y="5" width="11" height="8" rx="1" fill="#fff"/><path d="M3.8 5.4 9 9.6l5.2-4.2" fill="none" stroke="#6cc02a" stroke-width="1.2"/></svg>
        helen.dovbush@mailvane.example
      </li>
      <li>
        <svg viewBox="0 0 18 18"><rect width="18" height="18" rx="3" fill="#6cc02a"/><circle cx="9" cy="9" r="5" fill="none" stroke="#fff" stroke-width="1.3"/><ellipse cx="9" cy="9" rx="2" ry="5" fill="none" stroke="#fff" stroke-width="1.1"/><path d="M4 9h10" stroke="#fff" stroke-width="1.1"/></svg>
        www.qorvil.example
      </li>
    </ul>

    <div class="base-bar base-bar--green"></div>
    <div class="base-bar base-bar--grey"></div>
  </section>

  <section class="card card--back" aria-label="Business card back">
    <div class="back-texture" role="img" aria-label="Green background with a faint repeating pattern of three-line brand strokes"></div>
    <div class="back-brand">
      <div class="back-brand__row">
        <span class="back-brand__mark"></span>
        <span class="back-brand__name">qorvil</span>
      </div>
      <div class="back-brand__tagline">Electrical Wholesalers</div>
    </div>
  </section>

</main>
</body>
</html>
```